Farm Entrance Sign Design for Estate - Maplewick Meadow Farm

I am seeking a sign to hang where you turn in my driveway to my farm. The name of the farm is "Maplewick Meadow Farm". The sign/logo does not need the work "Farm" in it necessarily. The sign should be simple, clean, elegant.

I will attach some basic signs that are of the quality I am seeking. I will also attach a view of the farm entrance. I do not want the sign to compete with the landscape. This is in an area of estate type farms with horses and high end homes.

We are a cattle farm. But don't necessarily have to have cow on sign.

Font styles to use
Sans Serif

Colors

Designer to choose colors to be used in the design.

Requirements
Nice to have
• I prefer a clean font...nothing fancy

```html
<!DOCTYPE html>
<html lang="en">
<head>
<meta charset="utf-8">
<title>Maplewick Meadow Farm – Entrance Sign</title>
<link href="https://fonts.googleapis.com/css2?family=Saira+Extra+Condensed:wght@700&display=swap" rel="stylesheet">
<style>
  :root {
    --backdrop: #bdbdbf;
    --sign-face: #f7f9fa;
    --berry-red: #ed1c24;
    --field-green: #4a8a3f;
    --leaf-light: #b7d645;
    --leaf-dark: #3fa548;
    --illustration-tint: #fbe3e3;
  }
  html, body {
    margin: 0;
    padding: 0;
    width: 1200px;
    height: 1200px;
    overflow: hidden;
    background: var(--backdrop);
  }
  .sign-canvas {
    display: block;
    width: 1200px;
    height: 1200px;
  }
  .sign-face { fill: var(--sign-face); }
  .farm-name {
    font-family: "Saira Extra Condensed", "Arial Narrow", sans-serif;
    font-weight: 700;
  }
  .farm-name--primary { fill: var(--berry-red); }
  .farm-name--secondary { fill: var(--field-green); }
  .illustration-area { fill: var(--illustration-tint); }
</style>
</head>
<body>
<svg class="sign-canvas" viewBox="0 0 1932 1932" xmlns="http://www.w3.org/2000/svg">
  <defs>
    <linearGradient id="wave-back" x1="0" y1="0" x2="0" y2="1">
      <stop offset="0" stop-color="var(--leaf-light)" style="stop-color:#b7d645"/>
      <stop offset="0.45" stop-color="#b7d645"/>
      <stop offset="0.8" stop-color="#3fa548"/>
      <stop offset="1" stop-color="#3fa548"/>
    </linearGradient>
    <linearGradient id="wave-front" x1="0" y1="0" x2="1" y2="0">
      <stop offset="0" stop-color="#b7d645"/>
      <stop offset="0.4" stop-color="#a6cf45"/>
      <stop offset="1" stop-color="#3fa548"/>
    </linearGradient>
    <clipPath id="sign-clip">
      <rect x="324" y="324" width="1283" height="1283"/>
    </clipPath>
  </defs>

  <rect class="sign-face" x="324" y="324" width="1283" height="1283"/>

  <g class="corner-waves" clip-path="url(#sign-clip)">
    <g class="corner-wave corner-wave--top-left">
      <path fill="url(#wave-back)" d="M324 324 L860 324 C760 390 600 390 530 450 C460 510 460 580 475 650 C490 720 520 780 512 840 C505 900 470 920 440 945 C400 975 360 1000 324 1032 Z"/>
      <path fill="url(#wave-front)" d="M324 324 L775 324 C700 370 560 370 480 430 C420 475 425 540 440 600 C455 670 470 740 440 780 C420 805 360 825 324 845 Z"/>
    </g>
    <g class="corner-wave corner-wave--bottom-right" transform="rotate(180 965.5 965.5)">
      <path fill="url(#wave-back)" d="M324 324 L860 324 C760 390 600 390 530 450 C460 510 460 580 475 650 C490 720 520 780 512 840 C505 900 470 920 440 945 C400 975 360 1000 324 1032 Z"/>
      <path fill="url(#wave-front)" d="M324 324 L775 324 C700 370 560 370 480 430 C420 475 425 540 440 600 C455 670 470 740 440 780 C420 805 360 825 324 845 Z"/>
    </g>
  </g>

  <text class="farm-name farm-name--primary" x="578" y="648" font-size="222" textLength="929" lengthAdjust="spacingAndGlyphs">MAPLEWICK</text>
  <text class="farm-name farm-name--secondary" x="584" y="921" font-size="286" textLength="923" lengthAdjust="spacingAndGlyphs">MEADOW FARM</text>

  <rect class="illustration-area" x="472" y="995" width="618" height="540" rx="60"
        role="img" aria-label="Red line-art illustration of two strawberries with leafy tops"/>
</svg>
</body>
</html>
```